2026 Compostable Stand up Pouch Redesign

Project Overview
We are a natural dog bakery focused on simple, healthy ingredients and earth-friendly packaging. As the first step in a rebrand, we are redesigning our 6 oz stand-up pouch using new compostable packaging materials.
New pouch is the same size and structure as current (template provided)
Files included:
Existing Art template (PDF + JPG)
Photos of current packaging (for reference only)
Copy of existing logo (Meadowlark Treat Kitchen)
Copy of future logo (Birchwood Natural Bakery)
This redesign should feel like a clear upgrade—more refined, more intentional, and more aligned with sustainability.
⚠️ IMPORTANT LAYOUT CONSTRAINT (PLEASE READ)
The new pouch has a full-width horizontal window.
Design elements may ONLY appear above and below the window
No design elements can be placed to the left or right of the window
A 4.5" W x 3.5" H blank space above the window must be preserved
This is reserved for applied product labels
Keep this area completely clean (no textures, patterns, or graphics)
Submissions that ignore these elements will not be considered.
Brand Direction & Style
We are looking for a design that feels:
Natural and ingredient-focused
Eco-conscious and sustainable
Clean and elevated (not rustic, not overly playful)
Warm and trustworthy
Avoid:
Neon or bright artificial colors
Loud, busy, or overly commercial designs
Cartoon-heavy or overly whimsical styles
Color Direction
Our current packaging is kraft brown, but the new material allows full-color printing. We are looking for:
Nature-inspired colors only
Greens, muted blues, warm browns, soft earth tones
Background color is flexible within this palette
Must work with:
Current logo: Meadowlark Treat Kitchen
Future logo: Birchwood Natural Bakery
👉 For this project, use Meadowlark Treat Kitchen logo only
Front of Pouch Requirements
Do NOT include logo on pouch front
(Logo will be on applied labels)
Required Elements
Tagline: Simple, Healthy Ingredients. Earth Friendly Packaging.
Compostable Messaging (REQUIRED):
Must clearly communicate that packaging is compostable
Optional placement:
Tear-off strip near hang hole
BUT must also appear somewhere on the main pouch design
Origin Callout:
“Hand Made in the Pacific Northwest”
Can be a badge, stamp, or graphic (open to redesign)
Icons (Highly Encouraged)
We would like to explore a clean, minimal icon set for:
No Corn
No Wheat
No Soy
No GMOs
Compostable Packaging
(Keep icons simple, clean, and consistent with natural aesthetic)
Back of Pouch Requirements
Messaging Direction
Do NOT use: “The healthiest pet bakery in the US”
Instead, build around:
Simple, Healthy Ingredients. Earth Friendly Packaging.
Content
“Our Recipes” bullet points (from current packaging – still valid)
Sustainability messaging:
Include reference to reducing our “carbon pawprint”
Emphasize eco-friendly materials and practices
Design Direction
Open to new layout and graphics
Should visually reinforce:
Clean ingredients
Natural sourcing
Sustainability
Printing Considerations
Design should be mindful of production scalability:
Should translate well to both digital and roto printing
Avoid overly complex gradients or excessive color layering
Creative Freedom (Important)
While we have outlined structure and constraints, we are intentionally leaving visual interpretation open.
We welcome:
Fresh layout ideas
Refined graphic elements
Elevated visual storytelling
We are especially interested in designs that feel:
Thoughtful
Clean
Naturally premium
Any design submission that includes loud, neon, or "aggressive" color schemes or a mass market appeal will be eliminated immediately. We are a premium, natural dog bakery found in independent stores only.
UPDATED & IMPORTANT DESIGN REQUIREMENTS (PLEASE READ)
This pouch is a base design used across all flavors. A separate product label will be applied.
A clearly defined blank area must be left for label placement (do not incorporate into artwork).
The product viewing window is fixed:
Size and placement must match the template exactly
Do not resize, reposition, or redesign the window
Designs that do not follow these requirements will not be considered.
Please review the discussion board for additional feedback and direction before submitting revisions.

```html
<!DOCTYPE html>
<html lang="en">
<head>
<meta charset="utf-8">
<title>Compostable Stand-Up Pouch – Front</title>
<link href="https://fonts.googleapis.com/css2?family=Cormorant+Garamond:wght@500;600&family=EB+Garamond:wght@400;500&display=swap" rel="stylesheet">
<style>
  :root {
    --page-bg: #efedf0;
    --cream: #ece7da;
    --sage: #a8c699;
    --sage-deep: #8cb47c;
    --leaf: #5f9a48;
    --leaf-dark: #3f7a31;
    --ink-green: #2f4b33;
    --line: #6f8a6c;
    --origin-text: #f3f1e6;
    --treat-light: #c9a56b;
    --treat-dark: #8d6a3b;
  }
  * { box-sizing: border-box; margin: 0; padding: 0; }
  html, body { width: 1200px; height: 1200px; overflow: hidden; }
  body { background: var(--page-bg); position: relative; }

  .pouch {
    position: absolute; left: 260px; top: 50px;
    width: 680px; height: 1100px;
    border-radius: 14px 14px 10px 10px;
    overflow: hidden;
    background: var(--cream);
  }
  .tear-strip {
    position: absolute; left: 0; top: 0; width: 100%; height: 135px;
    background: var(--cream);
  }
  .tear-strip .perforation {
    position: absolute; left: 12px; right: 12px; top: 107px;
    border-top: 1.5px dashed #b9b3a4;
  }
  .tear-strip .compost-note {
    position: absolute; left: 50%; top: 96px; transform: translateX(-50%);
    background: var(--cream); padding: 0 12px;
    font: 400 16px/1 "EB Garamond", serif; color: #4d5a4c; letter-spacing: .4px;
  }
  .hang-hole {
    position: absolute; top: 92px; width: 10px; height: 10px; border-radius: 50%;
    background: var(--page-bg);
  }
  .label-zone {
    position: absolute; left: 0; top: 135px; width: 100%; height: 199px;
    background: var(--sage-deep);
  }
  .label-zone .blank-area {
    position: absolute; left: 28px; right: 28px; top: 30px; bottom: 0;
    background: var(--sage);
  }
  .zipper {
    position: absolute; left: 0; width: 100%; height: 2px; background: rgba(255,255,255,.35);
  }
  .window {
    position: absolute; left: 54px; right: 52px; top: 334px; height: 169px;
    background: var(--sage-deep);
  }
  .window .contents {
    position: absolute; inset: 0;
    background: radial-gradient(ellipse at 50% 45%, var(--treat-light), var(--treat-dark));
  }
  .window-sides {
    position: absolute; top: 334px; height: 169px; width: 54px; background: var(--sage-deep);
  }
  .message-panel {
    position: absolute; left: 0; top: 503px; width: 100%; height: 340px;
    background: var(--cream);
    text-align: center; color: var(--ink-green);
  }
  .tagline {
    position: absolute; left: 0; right: 0; top: 26px;
    font: 600 39px/51px "Cormorant Garamond", serif; letter-spacing: .4px;
  }
  .divider {
    position: absolute; left: 114px; right: 92px; top: 144px; height: 1px; background: var(--line);
  }
  .divider-mark {
    position: absolute; left: 50%; top: 137px; transform: translateX(-50%);
  }
  .sustain-copy {
    position: absolute; left: 0; right: 0; top: 157px;
    font: 400 22px/31px "EB Garamond", serif; letter-spacing: 1px;
  }
  .icon-row { position: absolute; left: 0; top: 234px; width: 100%; height: 80px; }
  .icon {
    position: absolute; width: 90px; margin-left: -45px; text-align: center;
  }
  .icon svg { display: block; margin: 0 auto; }
  .icon span {
    display: block; margin-top: 6px;
    font: 400 14.5px/1 "EB Garamond", serif; color: #4a5c49; letter-spacing: .3px;
  }
  .icon-sep { position: absolute; top: 4px; width: 1px; height: 46px; background: #b9bfae; }

  .origin-band {
    position: absolute; left: 0; top: 843px; width: 100%; height: 257px;
    background: linear-gradient(180deg, #8fbf73 0%, var(--leaf) 45%, var(--leaf-dark) 100%);
  }
  .origin-band .rule { position: absolute; left: 0; right: 0; top: 0; height: 3px; background: #d9e5cd; }
  .origin-callout {
    position: absolute; left: 0; right: 0; top: 878px;
    text-align: center; color: var(--origin-text);
    font: 600 28px/36px "Cormorant Garamond", serif; letter-spacing: .6px;
  }
</style>
</head>
<body>
  <div class="pouch">
    <div class="tear-strip">
      <div class="perforation"></div>
      <div class="compost-note">100% Compostable</div>
    </div>
    <div class="hang-hole" style="left:-5px"></div>
    <div class="hang-hole" style="right:-5px"></div>

    <div class="label-zone">
      <div class="blank-area"></div>
      <div class="zipper" style="top:22px"></div>
      <div class="zipper" style="top:30px"></div>
    </div>

    <div class="window-sides" style="left:0"></div>
    <div class="window-sides" style="right:0"></div>
    <div class="window">
      <div class="contents" role="img" aria-label="Clear window showing bone-shaped baked dog treats"></div>
    </div>

    <div class="message-panel">
      <p class="tagline">Simple, Healthy Ingredients.<br>Earth Friendly Packaging.</p>
      <div class="divider"></div>
      <svg class="divider-mark" width="20" height="14" viewBox="0 0 20 14" aria-hidden="true">
        <path d="M1 4 L10 13 L19 4 L14 1 L6 1 Z" fill="var(--ink-green)"/>
      </svg>
      <p class="sustain-copy">100% Compostable Packaging<br>Designed to Reduce Our Carbon Pawprint</p>

      <div class="icon-row">
        <div class="icon-sep" style="left:238px"></div>
        <div class="icon-sep" style="left:325px"></div>
        <div class="icon-sep" style="left:412px"></div>
        <div class="icon-sep" style="left:508px"></div>

        <div class="icon" style="left:117px">
          <svg width="54" height="54" viewBox="0 0 54 54" aria-hidden="true">
            <circle cx="27" cy="27" r="24" fill="none" stroke="var(--ink-green)" stroke-width="2.5"/>
            <ellipse cx="27" cy="27" rx="7" ry="13" fill="none" stroke="var(--ink-green)" stroke-width="2"/>
            <line x1="10" y1="10" x2="44" y2="44" stroke="var(--ink-green)" stroke-width="2.5"/>
          </svg><span>No Corn</span>
        </div>
        <div class="icon" style="left:193px">
          <svg width="54" height="54" viewBox="0 0 54 54" aria-hidden="true">
            <circle cx="27" cy="27" r="24" fill="none" stroke="var(--ink-green)" stroke-width="2.5"/>
            <line x1="27" y1="12" x2="27" y2="42" stroke="var(--ink-green)" stroke-width="2"/>
            <path d="M27 18 l-6 -4 M27 18 l6 -4 M27 25 l-6 -4 M27 25 l6 -4 M27 32 l-6 -4 M27 32 l6 -4" stroke="var(--ink-green)" stroke-width="2" fill="none"/>
            <line x1="10" y1="10" x2="44" y2="44" stroke="var(--ink-green)" stroke-width="2.5"/>
          </svg><span>No Wheat</span>
        </div>
        <div class="icon" style="left:278px">
          <svg width="54" height="54" viewBox="0 0 54 54" aria-hidden="true">
            <circle cx="27" cy="27" r="24" fill="none" stroke="var(--ink-green)" stroke-width="2.5"/>
            <path d="M18 36 C14 28 22 20 28 16 C36 12 40 20 34 26 C30 30 30 36 24 38 C21 39 19 38 18 36 Z" fill="none" stroke="var(--ink-green)" stroke-width="2"/>
            <line x1="10" y1="10" x2="44" y2="44" stroke="var(--ink-green)" stroke-width="2.5"/>
          </svg><span>No Soy</span>
        </div>
        <div class="icon" style="left:365px">
          <svg width="54" height="54" viewBox="0 0 54 54" aria-hidden="true">
            <circle cx="27" cy="27" r="24" fill="none" stroke="var(--ink-green)" stroke-width="2.5"/>
            <path d="M20 14 C34 20 20 30 34 40 M34 14 C20 20 34 30 20 40" fill="none" stroke="var(--ink-green)" stroke-width="2"/>
            <line x1="10" y1="10" x2="44" y2="44" stroke="var(--ink-green)" stroke-width="2.5"/>
          </svg><span>No GMOs</span>
        </div>
        <div class="icon" style="left:456px">
          <svg width="54" height="54" viewBox="0 0 54 54" aria-hidden="true">
            <circle cx="27" cy="27" r="24" fill="none" stroke="var(--ink-green)" stroke-width="2.5"/>
            <path d="M18 36 C18 24 26 16 38 16 C38 28 30 36 18 36 Z M18 36 L32 22" fill="none" stroke="var(--ink-green)" stroke-width="2"/>
            <line x1="10" y1="10" x2="44" y2="44" stroke="var(--ink-green)" stroke-width="2.5"/>
          </svg><span>No GMOs</span>
        </div>
        <div class="icon" style="left:552px">
          <svg width="54" height="54" viewBox="0 0 54 54" aria-hidden="true">
            <circle cx="27" cy="27" r="24" fill="none" stroke="var(--ink-green)" stroke-width="2.5"/>
            <path d="M16 38 C16 24 26 16 40 15 C40 30 30 38 16 38 Z" fill="var(--ink-green)"/>
            <path d="M18 36 L34 21" stroke="var(--cream)" stroke-width="1.5"/>
          </svg><span>Compostable</span>
        </div>
      </div>
    </div>

    <div class="origin-band" role="img" aria-label="Soft watercolor green forest backdrop">
      <div class="rule"></div>
    </div>
    <p class="origin-callout">Hand Made in the<br>Pacific Northwest</p>
  </div>
</body>
</html>
```